KP Rubbish Removal Business Card

Hey,
I need a double sided business card designed for a rubbish removal business based in Australia. Logo is already chosen, similar colours preferred for both sides of the business card.

Details to include:

Front:

KP Rubbish Removal
Darren Holloway
Managing Director
Mobile: 0471 920 246
Email: darren@kprubbishremoval.com.au
Website: kprubbishremoval.com.au

Rear:

How did we do?
kprubbishremoval.com.au/review

```html
<!DOCTYPE html>
<html lang="en">
<head>
<meta charset="utf-8">
<title>KP Rubbish Removal Business Card</title>
<link rel="stylesheet" href="https://fonts.googleapis.com/css2?family=Oswald:wght@500&family=Roboto:wght@400;500;700&display=swap">
<style>
  :root {
    --bg: #e6ebe7;
    --green-dark: #1fa045;
    --green-light: #6db543;
    --green-text: #3aa63a;
    --grey-text: #555a5e;
    --grey-line: #b8b8b8;
    --card-white: #f4f4f4;
    --white: #ffffff;
  }
  * { margin: 0; padding: 0; box-sizing: border-box; }
  html, body { width: 1200px; height: 944px; overflow: hidden; }
  body {
    background: var(--bg);
    font-family: "Roboto", Arial, sans-serif;
    display: flex;
    flex-direction: column;
    align-items: center;
    justify-content: center;
    gap: 40px;
  }
  .card {
    position: relative;
    width: 700px;
    height: 428px;
    overflow: hidden;
    box-shadow: 0 4px 14px rgba(0,0,0,0.12);
  }

  /* Rear side */
  .card-rear {
    background: linear-gradient(200deg, var(--green-light) 0%, var(--green-dark) 100%);
    color: var(--white);
  }
  .review-title {
    position: absolute;
    left: 70px;
    top: 110px;
    font-family: "Oswald", "Arial Narrow", sans-serif;
    font-weight: 500;
    line-height: 0.9;
    text-transform: uppercase;
  }
  .review-title .small { display: block; font-size: 62px; letter-spacing: -1px; }
  .review-title .big { display: block; font-size: 150px; letter-spacing: -3px; }
  .review-prompt {
    position: absolute;
    left: 330px;
    top: 160px;
    text-align: center;
    width: 330px;
  }
  .review-prompt .rule {
    display: block;
    width: 70px;
    height: 3px;
    background: var(--white);
    margin: 0 auto;
  }
  .review-prompt .question {
    font-weight: 500;
    font-size: 34px;
    letter-spacing: 0.5px;
    margin-top: 14px;
  }
  .review-prompt .url {
    font-weight: 500;
    font-size: 14px;
    letter-spacing: 0.3px;
    text-transform: uppercase;
    margin: 4px 0 16px;
  }

  /* Front side */
  .card-front { background: var(--card-white); }
  .card-front .wave { position: absolute; inset: 0; }
  .brand-mark {
    position: absolute;
    left: 60px;
    top: 100px;
    width: 240px;
    display: flex;
    flex-direction: column;
    align-items: center;
    gap: 12px;
    color: var(--green-text);
    font-weight: 700;
    font-size: 20px;
    text-align: center;
  }
  .brand-mark .dot {
    width: 70px; height: 70px; border-radius: 50%;
    background: var(--green-dark);
  }
  .divider {
    position: absolute;
    left: 320px; top: 62px;
    width: 1px; height: 170px;
    background: var(--grey-line);
  }
  .contact { position: absolute; left: 345px; top: 60px; color: var(--grey-text); }
  .contact .name { color: var(--green-text); font-weight: 700; font-size: 30px; }
  .contact .role { font-size: 18px; margin: 2px 0 16px; }
  .contact ul { list-style: none; }
  .contact li { display: flex; align-items: center; gap: 10px; font-size: 17px; margin-bottom: 6px; }
  .contact svg { width: 16px; height: 16px; fill: var(--green-dark); flex: none; }
  .company-band {
    position: absolute;
    left: 34px; bottom: 16px;
    color: var(--white);
    font-weight: 500;
    font-size: 24px;
    letter-spacing: 0.5px;
    text-transform: uppercase;
  }
</style>
</head>
<body>

<section class="card card-rear" aria-label="Business card rear">
  <h1 class="review-title"><span class="small">Review</span><span class="big">Us!</span></h1>
  <div class="review-prompt">
    <span class="rule"></span>
    <p class="question">HOW DID WE DO?</p>
    <p class="url">kprubbishremoval.com.au/review</p>
    <span class="rule"></span>
  </div>
</section>

<section class="card card-front" aria-label="Business card front">
  <svg class="wave" viewBox="0 0 700 428" preserveAspectRatio="none" aria-hidden="true">
    <defs>
      <linearGradient id="band-green" x1="0" y1="1" x2="1" y2="0">
        <stop offset="0" stop-color="#1fa045"/>
        <stop offset="1" stop-color="#6db543"/>
      </linearGradient>
    </defs>
    <path d="M440 290 C 560 270, 650 235, 700 185 L700 205 C 650 245, 560 278, 440 290 Z" fill="#b8b8b8"/>
    <path d="M0 428 L0 360 C 140 335, 300 305, 440 290 C 560 276, 650 245, 700 205 L700 428 Z" fill="url(#band-green)"/>
  </svg>

  <div class="brand-mark">
    <span class="dot"></span>
    <span>KP Rubbish Removal</span>
  </div>

  <div class="divider"></div>

  <div class="contact">
    <p class="name">Darren Holloway</p>
    <p class="role">Managing Director</p>
    <ul>
      <li><svg viewBox="0 0 16 16"><path d="M3.5 1l2.5 3-1.5 1.8c.8 2 2.4 3.6 4.5 4.5L10.8 9l3.2 2.4-1.2 2.8C7 14 2 9 1.8 3.2z"/></svg>0471 920 246</li>
      <li><svg viewBox="0 0 16 16"><path d="M1 3h14v10H1z M1 3l7 6 7-6" stroke="#f4f4f4" stroke-width="1.2"/></svg>darren@kprubbishremoval.com.au</li>
      <li><svg viewBox="0 0 16 16"><circle cx="8" cy="8" r="7"/><path d="M1 8h14M8 1c-3 3.5-3 10.5 0 14M8 1c3 3.5 3 10.5 0 14" stroke="#f4f4f4" stroke-width="1" fill="none"/></svg>www.kprubbishremoval.com.au</li>
    </ul>
  </div>

  <p class="company-band">KP Rubbish Removal</p>
</section>

</body>
</html>
```